Tirovel

We need a business card for our company is a holding for different business all are different we try to have some air of relax and fun in our projects we add pictures of the office to give you an idea od the mood of the business

Business

```html
<!DOCTYPE html>
<html lang="en">
<head>
<meta charset="utf-8">
<title>Tirovel — Business Card</title>
<link rel="stylesheet" href="https://fonts.googleapis.com/css2?family=Exo+2:wght@400;600;700&display=swap">
<style>
  :root {
    --backdrop: #e9e4da;
    --card: #ffffff;
    --card-shade: #ececec;
    --ink: #3b3b3b;
    --ink-soft: #6a6a6a;
    --brand-yellow: #f7e63a;
    --brand-brown: #5a3b1e;
    --logo-ink: #4a2f14;
  }
  * { box-sizing: border-box; margin: 0; padding: 0; }
  html, body {
    width: 1057px; height: 1200px; overflow: hidden;
    background: var(--backdrop);
    font-family: "Exo 2", sans-serif;
  }
  .sheet {
    width: 1057px; height: 1200px;
    display: flex; align-items: center; justify-content: center; gap: 60px;
  }
  .card {
    position: relative;
    width: 440px; height: 770px;
    background: radial-gradient(ellipse at 35% 30%, var(--card) 0%, var(--card) 45%, var(--card-shade) 100%);
    box-shadow: 0 14px 34px rgba(60, 45, 20, 0.28);
    overflow: hidden;
  }
  .brand {
    display: flex; align-items: center; gap: 12px;
    color: var(--logo-ink);
    font-weight: 700;
    letter-spacing: -0.5px;
  }
  .brand-square {
    background: var(--brand-yellow);
    flex: none;
  }
  /* front */
  .card-front .brand { position: absolute; top: 50px; left: 44px; font-size: 40px; }
  .card-front .brand-square { width: 34px; height: 34px; }
  .edge-stripe {
    position: absolute; top: 0; right: 48px; width: 30px; height: 100%;
    display: flex; flex-direction: column;
  }
  .edge-stripe .stripe-brown { background: var(--brand-brown); height: 52%; }
  .edge-stripe .stripe-yellow {
    background: var(--brand-yellow); flex: 1;
    display: flex; flex-direction: column; justify-content: flex-end; align-items: center;
    gap: 20px; padding-bottom: 158px;
  }
  .stripe-yellow svg { width: 16px; height: 16px; fill: none; stroke: #fff; stroke-width: 2; }
  .contact {
    position: absolute; right: 96px; top: 330px;
    text-align: right; color: var(--ink);
  }
  .contact .person { font-size: 27px; font-weight: 600; letter-spacing: 1px; }
  .contact .role { font-size: 12px; letter-spacing: 1.5px; color: var(--ink-soft); margin-top: 2px; }
  .contact .lines { margin-top: 30px; font-size: 15px; line-height: 36px; color: var(--ink-soft); letter-spacing: 0.5px; }
  .address {
    position: absolute; right: 96px; bottom: 80px;
    text-align: right; color: var(--ink); font-size: 22px; line-height: 32px; letter-spacing: 0.5px;
  }
  /* back */
  .card-back { display: flex; align-items: center; justify-content: center; }
  .card-back .brand { font-size: 52px; }
  .card-back .brand-square { width: 44px; height: 44px; }
</style>
</head>
<body>
<main class="sheet">
  <section class="card card-front" aria-label="Card front">
    <div class="brand"><span class="brand-square"></span>Tirovel</div>

    <div class="edge-stripe">
      <div class="stripe-brown"></div>
      <div class="stripe-yellow">
        <svg viewBox="0 0 16 16" aria-label="phone"><path d="M4 2h3l1 3-2 1a8 8 0 0 0 4 4l1-2 3 1v3a1 1 0 0 1-1 1A12 12 0 0 1 3 3a1 1 0 0 1 1-1z"/></svg>
        <svg viewBox="0 0 16 16" aria-label="mobile"><rect x="4.5" y="1.5" width="7" height="13" rx="1.5"/><path d="M7 12.5h2"/></svg>
        <svg viewBox="0 0 16 16" aria-label="email"><rect x="1.5" y="3.5" width="13" height="9"/><path d="M1.5 3.5 8 9l6.5-5.5"/></svg>
        <svg viewBox="0 0 16 16" aria-label="website"><circle cx="8" cy="8" r="6.5"/><path d="M1.5 8h13M8 1.5c3 3 3 10 0 13M8 1.5c-3 3-3 10 0 13"/></svg>
        <svg viewBox="0 0 16 16" aria-label="address"><path d="M8 15s5-5 5-8.5a5 5 0 0 0-10 0C3 10 8 15 8 15z"/><circle cx="8" cy="6.5" r="1.8"/></svg>
      </div>
    </div>

    <div class="contact">
      <p class="person">MARA LINDQVIST</p>
      <p class="role">GENERAL MANAGER</p>
      <div class="lines">
        <p>014 552 0931</p>
        <p>014 552 0932</p>
        <p>hello@tirovel.com</p>
        <p>www.tirovelgroup.com</p>
      </div>
    </div>

    <div class="address">
      <p>42 Harlow Lane</p>
      <p>5th Floor Block B</p>
    </div>
  </section>

  <section class="card card-back" aria-label="Card back">
    <div class="brand"><span class="brand-square"></span>Tirovel</div>
  </section>
</main>
</body>
</html>
```